Larkfield Capital Partners

We are a Private Equity firm that works with small companies. We have a mission of working with companies that help others in some way, shape, or form. If we feel that there is not a definitive way that the business helps others, we initiate a program of giving to others.

Target Market(s)

Our target market is small to mid size businesses. We do not have a certain business sector that we go after, but work with companies that have a niche.

Contact Information for Business Card

Currently very plain, black and white, standard print

Logo Text

Dedicated to Success

Requirements
Must have
• Want the color(s) and scheme to give off the feeling of openness to change, smart and sharp look, with a monogrammed type logo
Nice to have
• It would be nice to have a simple and look of distinction. We operate the Private Equity Firm as a virtual office and bring in best in class partners to work on projects as partners.
Should not have
• A wild and out of touch look.

```html
<!DOCTYPE html>
<html lang="en">
<head>
<meta charset="utf-8">
<title>Larkfield Capital Partners – Business Cards</title>
<link rel="stylesheet" href="https://fonts.googleapis.com/css2?family=Nunito+Sans:wght@400;600;700&display=swap">
<style>
  :root {
    --backdrop: #d9d4cc;
    --card: #ffffff;
    --navy: #1f3b57;
    --sky: #4aa3e6;
    --charcoal: #2e2e2e;
    --slate: #6b6b6b;
    --ink: #222222;
  }
  * { margin: 0; padding: 0; box-sizing: border-box; }
  html, body { width: 1200px; height: 760px; overflow: hidden; }
  body {
    background: var(--backdrop);
    font-family: "Nunito Sans", Arial, sans-serif;
    color: var(--ink);
  }
  .sheet {
    width: 1200px; height: 760px;
    display: grid;
    grid-template-columns: 500px 500px;
    grid-template-rows: 286px 286px;
    gap: 50px 60px;
    justify-content: center;
    align-content: center;
  }
  .card {
    background: var(--card);
    box-shadow: 0 6px 18px rgba(0,0,0,0.18);
    position: relative;
  }
  .card--blue { --mark: var(--navy); --accent: var(--sky); }
  .card--grey { --mark: var(--charcoal); --accent: var(--charcoal); }

  /* front */
  .card-front { display: flex; align-items: center; justify-content: center; }
  .brand { display: flex; align-items: center; gap: 14px; color: var(--mark); }
  .brand-square { width: 26px; height: 26px; background: var(--mark); flex: none; }
  .brand-name { font-weight: 700; line-height: 1.05; text-transform: uppercase; letter-spacing: 0.5px; }
  .card-front .brand-name { font-size: 34px; }

  /* back */
  .card-back { display: flex; align-items: center; padding: 0 30px 0 36px; }
  .card-back .brand { width: 170px; gap: 10px; }
  .card-back .brand-square { width: 16px; height: 16px; }
  .card-back .brand-name { font-size: 19px; }
  .divider { width: 2px; height: 174px; background: var(--ink); margin: 0 26px 0 18px; }
  .details { font-size: 12.5px; line-height: 1.5; }
  .person-name { font-size: 18px; font-weight: 600; letter-spacing: 0.5px; text-transform: uppercase; }
  .person-role { font-size: 15px; font-weight: 600; color: var(--accent); margin-bottom: 10px; }
  .address { font-weight: 600; }
  .contact-line { display: flex; align-items: center; gap: 8px; font-weight: 600; }
  .contact-line svg { width: 12px; height: 12px; flex: none; }
  .web { font-weight: 600; }
</style>
</head>
<body>
<main class="sheet">
  <section class="card card--blue card-front">
    <div class="brand"><span class="brand-square"></span><span class="brand-name">Larkfield<br>Capital Partners</span></div>
  </section>

  <section class="card card--grey card-front">
    <div class="brand"><span class="brand-square"></span><span class="brand-name">Larkfield<br>Capital Partners</span></div>
  </section>

  <section class="card card--blue card-back">
    <div class="brand"><span class="brand-square"></span><span class="brand-name">Larkfield<br>Capital Partners</span></div>
    <div class="divider"></div>
    <div class="details">
      <p class="person-name">Daniel Hart</p>
      <p class="person-role">Director</p>
      <p class="address">48, Alder Court<br>Brook Lane, CA 94012</p>
      <p class="contact-line"><svg viewBox="0 0 12 12"><rect x="2.5" y="0.5" width="7" height="11" rx="1" fill="none" stroke="currentColor" stroke-width="1.4"/><rect x="4.5" y="8.5" width="3" height="1.2" fill="currentColor"/></svg>410 . 555 .0172</p>
      <p class="contact-line"><svg viewBox="0 0 12 12"><rect x="0.7" y="2.5" width="10.6" height="7.5" fill="none" stroke="currentColor" stroke-width="1.4"/><path d="M1 3 L6 7 L11 3" fill="none" stroke="currentColor" stroke-width="1.4"/></svg>info@larkfieldcapital.com</p>
      <p class="web">www.larkfieldcapital.com</p>
    </div>
  </section>

  <section class="card card--grey card-back">
    <div class="brand"><span class="brand-square"></span><span class="brand-name">Larkfield<br>Capital Partners</span></div>
    <div class="divider"></div>
    <div class="details">
      <p class="person-name">Daniel Hart</p>
      <p class="person-role">Director</p>
      <p class="address">48, Alder Court<br>Brook Lane, CA 94012</p>
      <p class="contact-line"><svg viewBox="0 0 12 12"><rect x="2.5" y="0.5" width="7" height="11" rx="1" fill="none" stroke="currentColor" stroke-width="1.4"/><rect x="4.5" y="8.5" width="3" height="1.2" fill="currentColor"/></svg>410 . 555 .0172</p>
      <p class="contact-line"><svg viewBox="0 0 12 12"><rect x="0.7" y="2.5" width="10.6" height="7.5" fill="none" stroke="currentColor" stroke-width="1.4"/><path d="M1 3 L6 7 L11 3" fill="none" stroke="currentColor" stroke-width="1.4"/></svg>info@larkfieldcapital.com</p>
      <p class="web">www.larkfieldcapital.com</p>
    </div>
  </section>
</main>
</body>
</html>
```